A clean crisp business card for a Landscape Construction company. Designed to be easy to read contact/ info and also be appealing/interesting, unlike a traditional business card.

Industry/Entity Type

Landscape Construction

Contact Information for Business Card

Company name : Bramblecrest Landscape Construction, phone number: (877) 62Vales, website:Bramblecrestlandscapes.example, Email, sales@bramblecrestlandscapes.example

Requirements
Nice to have
• Luxurious finishes/ details…. Icons or emblems next to contact info
Should not have
• Clipart or general pictures

```html
<!DOCTYPE html>
<html lang="en">
<head>
<meta charset="utf-8">
<title>Bramblecrest Landscape Construction – Business Card</title>
<link rel="stylesheet" href="https://fonts.googleapis.com/css2?family=Cinzel:wght@600&family=Montserrat:wght@400;600&display=swap">
<style>
  :root{
    --stage:#b3b3b3;
    --paper:#ffffff;
    --ink:#3a3a3a;
    --night:#000000;
    --leaf:#a0cc3a;
    --leaf-soft:#c4e07f;
    --sky:#176bbf;
  }
  *{box-sizing:border-box;margin:0;padding:0}
  html,body{width:1000px;height:1200px;overflow:hidden;background:var(--stage)}
  .card{position:absolute;left:51px;width:899px;height:540px;overflow:hidden}
  .card--front{top:42px;background:var(--paper)}
  .card--back{top:616px;background:var(--night)}
  .waves{position:absolute;inset:0;width:100%;height:100%}
  .brand{position:absolute;text-align:center;font-family:"Cinzel",serif;font-weight:600;color:var(--sky)}
  .brand__dot{display:block;width:58px;height:58px;border-radius:50%;background:var(--leaf);margin:0 auto 18px}
  .brand__name{display:block;font-size:40px;line-height:1;letter-spacing:1px}
  .brand__line{display:block;font-size:15.5px;letter-spacing:3.4px;margin-top:8px}
  .card--front .brand{left:20px;top:58px;width:420px}
  .card--back .brand{left:240px;top:118px;width:420px}
  .corner-accent{position:absolute;left:759px;top:21px;width:120px;height:115px;
    background:linear-gradient(135deg,var(--leaf-soft),var(--leaf));opacity:.9}
  .contact{position:absolute;left:449px;top:237px;width:420px;height:192px;
    background:var(--paper);border-left:8px solid var(--leaf);border-bottom:8px solid var(--leaf);
    border-radius:16px;padding:10px 0 0 28px;font-family:"Montserrat",sans-serif;color:var(--ink)}
  .contact__name{font-size:21px;font-weight:600;line-height:1.1}
  .contact__role{font-size:17px;margin-top:3px;line-height:1.2}
  .contact__list{list-style:none;margin-top:2px}
  .contact__item{display:flex;align-items:center;gap:12px;font-size:15px;height:36px;white-space:nowrap}
  .contact__icon{width:18px;height:18px;flex:none;fill:none;stroke:var(--sky);stroke-width:1.6}
</style>
</head>
<body>

<section class="card card--front">
  <svg class="waves" viewBox="0 0 1062 638" preserveAspectRatio="none" aria-hidden="true">
    <path fill="#a0cc3a" d="M0 420 C140 510 270 555 420 552 C620 548 820 485 1000 485 L1062 515 L1062 538 C900 505 700 520 470 565 C300 590 140 575 0 538 Z"/>
    <path fill="#176bbf" d="M0 568 C200 620 420 590 640 565 C820 545 960 540 1062 570 L1062 638 L0 638 Z"/>
  </svg>
  <div class="corner-accent" role="img" aria-label="Green leaf ornament area"></div>
  <div class="brand">
    <span class="brand__dot"></span>
    <span class="brand__name">Bramblecrest</span>
    <span class="brand__line">LANDSCAPE CONSTRUCTION</span>
  </div>
  <div class="contact">
    <p class="contact__name">Your Name</p>
    <p class="contact__role">Position</p>
    <ul class="contact__list">
      <li class="contact__item">
        <svg class="contact__icon" viewBox="0 0 24 24"><path d="M6 3 L9 3 L10.5 8 L8.5 9.5 C9.5 12 12 14.5 14.5 15.5 L16 13.5 L21 15 L21 18 C21 19.5 20 20.5 18.5 20.5 C10 20 4 14 3.5 5.5 C3.5 4 4.5 3 6 3 Z"/></svg>
        (877) 62Vales
      </li>
      <li class="contact__item">
        <svg class="contact__icon" viewBox="0 0 24 24"><circle cx="12" cy="12" r="9"/><ellipse cx="12" cy="12" rx="4" ry="9"/><path d="M3 12 H21 M5 7 H19 M5 17 H19"/></svg>
        Bramblecrestlandscapes.example
      </li>
      <li class="contact__item">
        <svg class="contact__icon" viewBox="0 0 24 24"><rect x="3" y="6" width="18" height="12"/><path d="M3 6 L12 13 L21 6 M3 18 L10 11.5 M21 18 L14 11.5"/></svg>
        sales@bramblecrestlandscapes.example
      </li>
    </ul>
  </div>
</section>

<section class="card card--back">
  <svg class="waves" viewBox="0 0 1062 638" preserveAspectRatio="none" aria-hidden="true">
    <path fill="#a0cc3a" d="M0 508 C120 470 240 455 360 470 C520 490 660 545 820 545 C930 545 1000 480 1062 420 L1062 535 C960 575 860 595 760 590 C600 580 480 540 330 525 C200 512 90 525 0 538 Z"/>
    <path fill="#176bbf" d="M0 568 C160 540 300 540 470 560 C640 580 800 602 900 600 C980 598 1030 585 1062 572 L1062 638 L0 638 Z"/>
  </svg>
  <div class="brand">
    <span class="brand__dot"></span>
    <span class="brand__name">Bramblecrest</span>
    <span class="brand__line">LANDSCAPE CONSTRUCTION</span>
  </div>
</section>

</body>
</html>
```